Create Website for new company called "Verdant Lodge 17"

Verdant Lodge 17 is a new business situated in Southwestern Colorado. We are creating a business that will rent out spaces where clients can grow their own marijuana. Picture a large green house with partitioned spaces that are secured by a lock. Best way to envision this would be to think of a storage business that rents out storage rooms. The difference is that we will be having the units inside a green house ( for growing purposes) Picture a small area that is secured by locks, Picture an area that has the ability to provide state of the art security, cameras etc. We want to focus our efforts on professionals, blue collar workers and end users of marijuana. Our emphasis is in the area of assisting those whom wish to grow their own plants. We want to provide them a safe facility in which to do that. . Keep in mind that we also build custom grow rooms at clients homes and provide a grow pod (lease these) where a small grow unit will be delivered and picked up from our clients whom want to lease a unit for a short amount of time. We have a business card ( just designed) and will send that information to those whom express an interests in this project. We want to be able to sign people up for our services by entering an agreement and signing the agreement while on the internet. We want to provide our services to those whom consume recreational and medical marijuana. This site will need to gather information I.e email addresses so that we can followup with offers. This is a tremendous opportunity for the right designer. We will be creating many more websites as other states come on line and make marijuana legal to consume. Use the business card model for a point of reference of how we envision the concept. That is a business card we just recently printed. The hands and the plant is our logo so far. Open to suggestions. There will be three levels of service. Bronze, Silver, Gold or Platinum. We will also have a retail biz down the road but not at the present time.

Target Market(s)

Ages 21-60

Industry/Entity Type

Medical

Logo Text

Verdant Lodge 17.

Number of Pages Required

5+ page

Requirements
Must have
• Clean appearance not to busy , easily navigable from link to link, page to page. Must have ability down the road to enter into a contractual agreement via the website. Must use our provided logo and example of that is on our business card that will be uploaded here shortly. We would like to have the colors that are on the business card however if you have suggestions or color schemes that you want us to consider that is okay.
Nice to have
• Nice to have a animation of seed to weed and how clients can save a tremendous amount of money growing their own cannabis. Nice to have testimonial page or feedback page. Have a membership component to website,
Should not have
• No flashing lights, etc. Not to busy in terms of animations.

```html
<!DOCTYPE html>
<html lang="en">
<head>
<meta charset="utf-8">
<title>Verdant Lodge 17</title>
<link href="https://fonts.googleapis.com/css2?family=Ubuntu:wght@400;500;700&family=Source+Sans+3:wght@400;600;700&display=swap" rel="stylesheet">
<style>
:root{
  --green:#0e8a40;
  --green-dark:#0a6b31;
  --green-deep:#075a28;
  --orange:#cf7a2c;
  --orange-dark:#a85e1c;
  --ink:#222;
  --body:#3a3a3a;
  --footer:#3b3b3b;
  --footer-deep:#2d2d2d;
  --footer-text:#bdbdbd;
  --link:#1b4f9e;
}
*{margin:0;padding:0;box-sizing:border-box}
html,body{width:812px;height:1200px;overflow:hidden}
body{position:relative;font-family:"Source Sans 3",sans-serif;color:var(--body);background:#fff}
.abs{position:absolute}
h1,h2,h3,.nav a,.hero-caption{font-family:"Ubuntu",sans-serif}

/* header */
.site-header{left:0;top:0;width:812px;height:65px;background:linear-gradient(#16974a,var(--green-dark));box-shadow:0 2px 4px rgba(0,0,0,.3);z-index:3}
.brand{left:89px;top:0;width:141px;height:77px;background:#fff;box-shadow:0 2px 5px rgba(0,0,0,.35);z-index:4;display:flex;flex-direction:column;align-items:center;justify-content:center;gap:6px}
.brand-mark{display:block;width:18px;height:18px;border-radius:50%;background:var(--green)}
.brand-name{font-family:"Ubuntu",sans-serif;font-weight:700;font-size:13px;color:var(--ink);letter-spacing:.2px}
.account{left:628px;top:4px;width:95px;height:16px;background:#fff;border-radius:0 0 2px 2px;font-size:8.5px;color:var(--ink);display:flex;align-items:center;justify-content:center;gap:5px;z-index:4}
.nav{left:310px;top:34px;z-index:4;display:flex;align-items:center}
.nav a{color:#fff;font-size:10px;font-weight:500;text-decoration:none;margin-right:19px;line-height:21px}
.nav a.active{background:linear-gradient(#fff,#e6e6e6);color:var(--orange);width:51px;text-align:center;border-radius:2px}
.nav a:last-child{margin-right:0}

/* hero */
.hero{left:0;top:65px;width:812px;height:291px;background:radial-gradient(ellipse at 62% 45%,#7fa64e 0%,#4f7f2a 30%,#2f5e1c 60%,#1d3f12 100%)}
.hero-caption{left:89px;top:216px;width:330px;height:98px;background:rgba(20,30,18,.82);border-top:2px solid var(--orange);padding:12px 15px}
.hero-caption h1{font-size:23px;font-weight:500;color:#fff}
.hero-caption h1 span{color:#1fa052}
.hero-caption p{margin-top:8px;font-size:14px;line-height:20px;color:#d9d9d9}

/* welcome */
.welcome{left:0;top:356px;width:812px;height:186px;background:linear-gradient(#fff,#e3e3e3)}
.welcome h2{left:89px;top:25px;font-size:22px;font-weight:500;color:var(--ink)}
.welcome h2 span{color:var(--green)}
.rule{height:1px;background:#bdbdbd}
.rule::before{content:"";display:block;width:72px;height:2px;background:#555;margin-top:-1px}
.welcome .rule{left:89px;top:57px;width:379px}
.welcome p{left:89px;top:73px;width:379px;font-size:8.4px;line-height:14.8px;text-align:justify}
.video{left:510px;top:29px;width:204px;height:121px;background:#111}
.video-title{height:17px;color:#fff;font-size:8px;line-height:17px;padding-left:5px}
.video-frame{left:0;top:17px;width:204px;height:81px;background:linear-gradient(120deg,#3f6a2b,#5f8c3c 45%,#2b4c1d)}
.video-bar{left:0;top:98px;width:204px;height:23px;background:#1e1e1e;color:#ddd;font-size:6.5px;display:flex;align-items:center;gap:10px;padding-left:14px}
.shelf{left:500px;top:150px;width:222px;height:6px;background:linear-gradient(#e0a35a,#8b5a22);border-radius:3px;box-shadow:0 6px 8px rgba(0,0,0,.25)}

/* services */
.services{left:0;top:542px;width:812px;height:252px;background:linear-gradient(#13914a,var(--green-deep))}
.service{width:180px;text-align:center;color:#fff}
.service .badge{width:80px;height:80px;border-radius:50%;background:#f3f3f3;margin:0 auto;padding:6px;box-shadow:0 3px 5px rgba(0,0,0,.25)}
.service .badge div{width:68px;height:68px;border-radius:50%;background:radial-gradient(circle at 50% 40%,#de8d3e,var(--orange-dark));display:flex;align-items:center;justify-content:center}
.service h3{margin-top:13px;font-size:14.5px;font-weight:400}
.service p{margin:8px auto 0;width:155px;font-size:8px;line-height:14.4px;color:#cfe8d7}

/* news & testimonials */
.info{left:0;top:794px;width:812px;height:186px;background:linear-gradient(#dedede,#fafafa)}
.info h2{font-size:18px;font-weight:500;color:var(--green)}
.arrows{display:flex;gap:1px}
.arrows span{width:11px;height:11px;display:flex;align-items:center;justify-content:center}
.arrows .prev{background:#888}
.arrows .next{background:var(--orange)}
.news-photo{left:89px;top:67px;width:124px;height:88px;background:linear-gradient(#d6dbe0 0%,#b9c3c9 40%,#4e8a36 62%,#2f6a22 100%);border:1px solid #999}
.news h3{left:226px;top:72px;font-family:"Source Sans 3",sans-serif;font-weight:700;font-size:11px;color:var(--ink)}
.news p{left:226px;top:91px;width:244px;font-size:8px;line-height:14px}
.news a{left:226px;top:149px;font-size:8.4px;color:var(--link);text-decoration:none}
.quote{left:497px;top:70px;width:226px;font-size:8.2px;line-height:13.4px}
.quote-name{left:497px;top:126px;font-size:9px;color:var(--orange)}

/* footer */
.footer{left:0;top:980px;width:812px;height:178px;background:var(--footer)}
.footer h2{font-size:14px;font-weight:500;color:#fff}
.quick{left:89px;top:20px}
.quick ul{list-style:none;margin-top:12px}
.quick li{font-size:8.2px;color:var(--footer-text);line-height:16.5px;padding-left:15px;position:relative}
.quick li::before{content:"";position:absolute;left:0;top:5px;border-left:4px solid #aaa;border-top:3px solid transparent;border-bottom:3px solid transparent}
.newsletter{left:228px;top:20px;width:140px}
.newsletter p{margin-top:12px;font-size:6.6px;line-height:12px;color:#999}
.newsletter .field{margin-top:10px;width:138px;height:19px;background:#5a5a5a;border:1px solid #666;border-radius:2px;font-size:7px;color:#cfcfcf;padding:5px 7px}
.newsletter .submit{margin-top:12px;width:62px;height:19px;background:linear-gradient(#fff,#ddd);border-radius:2px;font-size:9px;font-weight:700;color:var(--ink);text-align:center;line-height:19px}
.contact-box{left:401px;top:42px;width:168px;height:115px;background:#474747}
.contact-title{left:414px;top:20px}
.contact-row{left:414px;display:flex;align-items:flex-start;gap:10px;font-size:8px;line-height:12px;color:var(--footer-text)}
.contact-row svg{flex:none}
.map{left:577px;top:52px;width:146px;height:80px;background:linear-gradient(135deg,#f1efe8,#e4e0d4);border:1px solid #888}
.map-link{left:579px;top:134px;font-size:6.6px;color:#aaa}
.bottom{left:0;top:1158px;width:812px;height:42px;background:var(--footer-deep);color:#d5d5d5}
.copyright{left:89px;top:15px;font-size:8.2px}
.follow{left:584px;top:12px;display:flex;align-items:center;gap:5px;font-size:11px}
.follow span.dot{width:16px;height:16px;border-radius:50%;display:inline-block}
</style>
</head>
<body>

<header class="site-header abs"></header>
<div class="brand abs">
  <span class="brand-mark"></span>
  <span class="brand-name">VERDANT LODGE 17</span>
</div>
<div class="account abs">
  <svg width="7" height="8" viewBox="0 0 7 8"><rect x="0" y="3.5" width="7" height="4.5" fill="#222"/><path d="M1.5 3.5V2.3a2 2 0 0 1 4 0v1.2" fill="none" stroke="#222" stroke-width="1"/></svg>
  <span>Login</span><span>|</span><span>Register</span>
</div>
<nav class="nav abs">
  <a class="active" href="#">Home</a>
  <a href="#">About Us</a>
  <a href="#">Services</a>
  <a href="#">Learning Center</a>
  <a href="#">News</a>
  <a href="#">Contact Us</a>
</nav>

<section class="hero abs" role="img" aria-label="Close-up photo of a cannabis leaf held between fingers in a grow room"></section>
<div class="hero-caption abs">
  <h1>We are a <span>VERDANT LODGE</span></h1>
  <p>Rent Out Spaces Where Clients can Grow Their Own Marijuana</p>
</div>

<section class="welcome abs">
  <h2 class="abs">Welcome to <span>VERDANT LODGE 17</span></h2>
  <div class="rule abs"></div>
  <p class="abs">Lorem Ipsum is simply dummy text of the printing and typesetting industry. Lorem Ipsum has been the industry's standard dummy text ever since the 1500s, when an unknown printer took a galley of type and scrambled it to make a type specimen book. It has survived not only five centuries, but also the leap into electronic typesetting, remaining essentially unchanged. It was popularised in the 1960s with the release of Typeline sheets containing Lorem Ipsum passages, and more recently with desktop publishing software like Quillset Layout including versions of Lorem Ipsum.</p>
  <div class="video abs">
    <div class="video-title">VERDANT LODGE 17</div>
    <div class="video-frame abs" role="img" aria-label="Video still of a hand holding a cannabis leaf">
      <svg class="abs" style="left:88px;top:26px" width="28" height="28" viewBox="0 0 28 28"><circle cx="14" cy="14" r="14" fill="rgba(0,0,0,.55)"/><path d="M11 8l9 6-9 6z" fill="#fff"/></svg>
    </div>
    <div class="video-bar abs">
      <svg width="8" height="8" viewBox="0 0 8 8"><path d="M0 0l8 4-8 4z" fill="#ccc"/></svg>
      <svg width="10" height="8" viewBox="0 0 10 8"><path d="M0 2.5h2.5L5.5 0v8L2.5 5.5H0z" fill="#ccc"/></svg>
      <span>0:00 / 0:30</span>
    </div>
  </div>
  <div class="shelf abs"></div>
</section>

<section class="services abs">
  <div class="service abs" style="left:82px;top:46px">
    <div class="badge"><div>
      <svg width="30" height="34" viewBox="0 0 30 34"><rect x="2" y="1" width="26" height="32" rx="2" fill="none" stroke="#fff" stroke-width="2.5"/><path d="M8 9h14M8 15h14M8 20h14M8 25h8" stroke="#fff" stroke-width="2.5"/></svg>
    </div></div>
    <h3>LEASE</h3>
    <p>Lorem Ipsum is simply dummy text of the printing and typesetting industry. Lorem Ipsum has been the industry's</p>
  </div>
  <div class="service abs" style="left:316px;top:46px">
    <div class="badge"><div>
      <svg width="30" height="34" viewBox="0 0 30 34"><path d="M8 15V10a7 7 0 0 1 14 0v5" fill="none" stroke="#fff" stroke-width="3.5"/><rect x="3" y="15" width="24" height="18" rx="2" fill="#fff"/><circle cx="15" cy="23" r="2.5" fill="#b46620"/><rect x="14" y="23" width="2" height="5" fill="#b46620"/></svg>
    </div></div>
    <h3>LOCK</h3>
    <p>Lorem Ipsum is simply dummy text of the printing and typesetting industry. Lorem Ipsum has been the industry's</p>
  </div>
  <div class="service abs" style="left:550px;top:46px">
    <div class="badge"><div>
      <svg width="34" height="28" viewBox="0 0 34 28"><path d="M2 7h8l3-5h8l3 5h8v19H2z" fill="#fff"/><circle cx="17" cy="16" r="7" fill="#b46620"/><circle cx="17" cy="16" r="4.5" fill="#fff"/></svg>
    </div></div>
    <h3>CAMERA</h3>
    <p>Lorem Ipsum is simply dummy text of the printing and typesetting industry. Lorem Ipsum has been the industry's</p>
  </div>
</section>

<section class="info abs">
  <h2 class="abs" style="left:89px;top:20px">Letest News</h2>
  <div class="arrows abs" style="left:446px;top:25px">
    <span class="prev"><svg width="6" height="6" viewBox="0 0 6 6"><path d="M4 0L1 3l3 3" fill="none" stroke="#fff" stroke-width="1.3"/></svg></span>
    <span class="next"><svg width="6" height="6" viewBox="0 0 6 6"><path d="M2 0l3 3-3 3" fill="none" stroke="#fff" stroke-width="1.3"/></svg></span>
  </div>
  <div class="rule abs" style="left:89px;top:50px;width:379px"></div>
  <div class="news">
    <div class="news-photo abs" role="img" aria-label="Photo of a worker inspecting rows of plants inside a greenhouse"></div>
    <h3 class="abs">There are many variations of passages.</h3>
    <p class="abs">Lorem Ipsum has been the industry's standard dummy text ever since the 1500s, when an unknown printer took a galley of type and scrambled it to make a type specimen book. It has survived not only five centuries.</p>
    <a class="abs" href="#">Read More &raquo;</a>
  </div>

  <h2 class="abs" style="left:497px;top:20px">What People Say</h2>
  <div class="arrows abs" style="left:700px;top:25px">
    <span class="prev"><svg width="6" height="6" viewBox="0 0 6 6"><path d="M4 0L1 3l3 3" fill="none" stroke="#fff" stroke-width="1.3"/></svg></span>
    <span class="next"><svg width="6" height="6" viewBox="0 0 6 6"><path d="M2 0l3 3-3 3" fill="none" stroke="#fff" stroke-width="1.3"/></svg></span>
  </div>
  <div class="rule abs" style="left:497px;top:50px;width:226px"></div>
  <p class="quote abs">&ldquo; Lorem Ipsum has been the industry's standard dummy text ever since the 1500s, when an unknown printer took a galley of type and scrambled it to make a type specimen book. It has survived not only five centuries. &rdquo;</p>
  <div class="quote-name abs">Tobias Wrenfield</div>
</section>

<footer class="footer abs">
  <div class="quick abs">
    <h2>Quick Links</h2>
    <ul><li>Home</li><li>About Us</li><li>Services</li><li>Learning Center</li><li>News</li><li>Contact Us</li></ul>
  </div>
  <div class="newsletter abs">
    <h2>Newsletter</h2>
    <p>Lorem Ipsum is simply dummy text of the printing and typesetting industry.</p>
    <div class="field">Email Address</div>
    <div class="submit">Submit</div>
  </div>
  <div class="contact-box abs"></div>
  <h2 class="contact-title abs">Contact Us</h2>
  <div class="contact-row abs" style="top:57px">
    <svg width="10" height="13" viewBox="0 0 10 13"><path d="M5 0a5 5 0 0 1 5 5c0 3.5-5 8-5 8S0 8.5 0 5a5 5 0 0 1 5-5z" fill="#eee"/><circle cx="5" cy="5" r="2" fill="#474747"/></svg>
    <span>Simply dummy text of the<br>Pinecrest, CO 81990</span>
  </div>
  <div class="contact-row abs" style="top:99px">
    <svg width="10" height="12" viewBox="0 0 10 12"><path d="M2 0l2.5 3-1.5 1.5c.8 1.8 1.9 3 3.5 3.8L8 7l2 2.5L8.5 12C4 11 0 6 0 1.5z" fill="#eee"/></svg>
    <span>1-855-555-0147</span>
  </div>
  <div class="contact-row abs" style="top:127px">
    <svg width="10" height="8" viewBox="0 0 10 8"><rect width="10" height="8" fill="#eee"/><path d="M0 0l5 4 5-4" fill="none" stroke="#474747" stroke-width="1"/></svg>
    <span>info@verdantlodge17.com</span>
  </div>
  <div class="map abs" role="img" aria-label="Street map showing the facility location"></div>
  <div class="map-link abs">View Area Map</div>
</footer>

<div class="bottom abs">
  <div class="copyright abs">Copyright @ 2014 Verdant Lodge 17</div>
  <div class="follow abs">
    <span style="margin-right:4px">Follow Us :</span>
    <span class="dot" style="background:#3b5a9a"></span>
    <span class="dot" style="background:#2ca6dc"></span>
    <span class="dot" style="background:#1176b0"></span>
    <span class="dot" style="background:#d02a25"></span>
  </div>
</div>

</body>
</html>
```